a little bit like bulkhop but selling small amounts of high end tech gear directly to customers inbox.

Hi Designers,

I have had my artflock logo attached to this project.
I have another web site (coolriver.com.au)which will be dedicated mostly to
enthusiast,s that want to water cool their pc's. It's not quite finished. I may
need your help with that one once we get Gizminibox up and running .I
like Rig Shell Depot layout for Coolriver
I want Gizmini to be simple to navigate, and similar to Bulkhop.
I will be selling Enthusiast PC Components in small volumes ie first in
best dressed. weekly specials,daily specials,free shipping
There should be the ability for me to upload the component photo direct
from my Orbit5 Phone .
Links to the manufacturers website and product reviews from vidstream
I will give you more in depth details tomorrow.

I would like my new site to be similar to e-Gadj.com.au but cooler! Added Sunday, October 1, 2017

Target Market(s)

Enthusiast PC Builders

Industry/Entity Type

Tech

Coding

Coded - Design and coding required

Number of Pages Required

1 page

Font styles to use
Sans Serif

Colors
33b8a4

Requirements
Must have
• Link the price of my product to pricora.com.au
• Drop down menus

```html
<!DOCTYPE html>
<html lang="en">
<head>
<meta charset="utf-8">
<title>Gizminibox – Enthusiast PC Components</title>
<link href="https://fonts.googleapis.com/css2?family=Open+Sans:wght@400;600;700&family=Roboto+Condensed:wght@400;700&display=swap" rel="stylesheet">
<style>
:root{
  --teal:#33b8a4;
  --teal-dark:#2a9c8b;
  --navy:#1d5a7c;
  --ink:#333;
  --muted:#777;
  --line:#e1e1e1;
  --bg-dark:#262626;
  --bar:#0b0b0b;
  --white:#fff;
  --price:#33b8a4;
  --star:#f0a22b;
}
*{box-sizing:border-box;margin:0;padding:0}
html,body{width:1200px;height:2922px;overflow:hidden}
body{position:relative;font-family:"Open Sans",Arial,sans-serif;color:var(--ink);
  background:linear-gradient(180deg,#2e2e2e 0%,#232323 40%,#2b2b2b 70%,#1f1f1f 100%)}
a{color:inherit;text-decoration:none}
.abs{position:absolute}

/* header */
.brand{left:97px;top:22px;width:320px;height:140px;display:flex;flex-direction:column;align-items:center}
.brand-mark{width:70px;height:70px;border-radius:50%;background:var(--teal)}
.brand-name{margin-top:10px;font-family:"Open Sans",sans-serif;font-weight:700;font-size:40px;color:var(--teal);letter-spacing:-0.5px;line-height:1}
.toplinks{right:97px;top:52px;display:flex;gap:28px;align-items:center;font-family:"Roboto Condensed",sans-serif;font-size:13px;color:#ddd;text-transform:uppercase}
.toplinks .phone{font-size:17px;font-weight:700;color:#fff}
.toplinks svg{vertical-align:-3px;margin-right:6px}
.mainnav{right:97px;top:112px;display:flex;gap:38px;font-family:"Roboto Condensed",sans-serif;font-size:15px;color:#fff;text-transform:uppercase}

/* bar */
.toolbar{left:0;top:182px;width:1200px;height:54px;background:var(--bar)}
.cat-head{left:97px;top:186px;width:221px;height:50px;background:var(--navy);display:flex;align-items:center;color:#fff;font-family:"Roboto Condensed",sans-serif;font-size:17px;text-transform:uppercase}
.cat-head .burger{width:50px;height:50px;background:#174b68;display:flex;align-items:center;justify-content:center;margin-right:24px}
.search{left:341px;top:190px;width:512px;height:40px;background:#fff;display:flex;font-size:12px;color:#888}
.search .q{flex:1;padding:12px 18px}
.search .cats{width:150px;border-left:1px solid var(--line);padding:12px 14px;text-transform:uppercase;font-size:11px;color:#555}
.search .go{width:44px;display:flex;align-items:center;justify-content:center;border-left:1px solid var(--line)}
.cart{left:900px;top:186px;width:201px;height:50px;background:var(--navy);display:flex;align-items:center;color:#fff;font-family:"Roboto Condensed",sans-serif;font-size:15px}
.cart .icon{width:64px;display:flex;justify-content:center;position:relative}
.cart .count{position:absolute;top:-8px;right:16px;width:16px;height:16px;border-radius:50%;background:var(--teal);font-size:10px;text-align:center;line-height:16px}

/* sidebar */
.sidebar{left:97px;top:236px;width:221px;height:1077px;background:#fff;list-style:none}
.sidebar li{height:37.8px;border-bottom:1px solid #ececec;display:flex;align-items:center;padding-left:16px;font-size:11.5px;color:#333;position:relative}
.sidebar li::before{content:"";width:5px;height:5px;border-top:1.5px solid #999;border-right:1.5px solid #999;transform:rotate(45deg);margin-right:14px}
.sidebar li:nth-child(-n+2){text-transform:uppercase}

/* slider */
.slider{left:343px;top:261px;width:758px;height:427px;border:4px solid #fff;background:radial-gradient(ellipse at 50% 70%,#2c6f8a 0%,#123a52 55%,#07192a 100%);color:#fff;text-align:center}
.slider h2{margin-top:50px;font-family:"Roboto Condensed",sans-serif;font-weight:700;font-size:50px;letter-spacing:1px}
.slider p{margin:10px auto 0;width:360px;font-family:"Roboto Condensed",sans-serif;font-weight:700;font-size:15px;line-height:22px;text-transform:uppercase}
.slider .arrow{position:absolute;top:210px;width:28px;height:28px;border:1.5px solid #fff;border-radius:50%;display:flex;align-items:center;justify-content:center}

/* promo banners */
.promo{top:711px;height:170px;overflow:hidden;border:3px solid #fff}
.promo .copy{position:absolute;left:0;top:0;width:62%;height:100%;background:var(--teal);padding:16px 18px;color:#fff;font-family:"Roboto Condensed",sans-serif;clip-path:polygon(0 0,100% 0,78% 100%,0 100%);z-index:1}
.promo .copy small{font-size:13px;text-transform:uppercase;display:block}
.promo .copy strong{font-size:20px;font-weight:400;text-transform:uppercase;display:block;margin-top:2px;white-space:nowrap}
.promo .btn{display:inline-block;margin-top:16px;background:#333;padding:5px 12px;font-size:12px;text-transform:uppercase}
.promo .photo{position:absolute;right:0;top:0;width:62%;height:100%}

/* section heads */
.sec-head{height:42px;background:#f1f1f1;display:flex;align-items:center;font-family:"Roboto Condensed",sans-serif;font-size:20px;text-transform:uppercase;color:#333;position:relative}
.sec-head .badge{width:42px;height:42px;background:var(--teal);display:flex;align-items:center;justify-content:center;margin-right:18px}
.sec-head .pager{position:absolute;right:10px;display:flex;gap:6px}
.sec-head .pager span{width:22px;height:22px;border:1px solid #999;border-radius:50%;display:flex;align-items:center;justify-content:center;font-size:14px;line-height:1}

/* products */
.product{background:#fff;text-align:center;position:relative;overflow:hidden}
.product .img{margin:0 auto}
.product .stars{font-size:11px;color:var(--star);letter-spacing:1px;margin-top:10px}
.product .stars i{color:#ccc;font-style:normal}
.product .name{font-size:12.5px;line-height:19px;color:#444;margin:8px auto 0;width:200px}
.product .price{margin-top:8px;font-size:17px}
.product .price b{color:var(--price);font-weight:600}
.product .price s{color:#555;font-size:13px}
.product .add{display:inline-block;margin-top:10px;border:1px solid #bbb;padding:5px 14px;font-size:11.5px;text-transform:uppercase;color:#555}
.ribbon{position:absolute;top:16px;left:-28px;width:110px;background:var(--teal);color:#fff;font-size:11px;text-align:center;transform:rotate(-45deg);padding:2px 0}

.weekly{left:343px;top:980px;width:758px;height:331px;display:flex;justify-content:space-between}
.weekly .product{width:232px;height:331px;padding-top:8px}
.weekly .product .name{margin-top:22px}
.panel{left:97px;width:1004px;background:#fff}
.panel .grid{display:flex}
.panel .product{flex:1;height:366px;border-right:1px solid var(--line);padding-top:28px}
.panel .product:last-child{border-right:0}

/* shipping band */
.band{left:0;top:2347px;width:1200px;height:189px;background:#6a6a6a}
.band .free{position:absolute;left:0;top:0;width:640px;height:189px;background:var(--teal);clip-path:polygon(0 0,100% 0,88% 100%,0 100%)}
.free-txt{left:97px;top:2385px;color:#fff;font-family:"Roboto Condensed",sans-serif}
.free-txt b{display:block;font-size:42px;line-height:40px;letter-spacing:2px}
.free-txt span{display:block;font-size:19px;margin-top:8px;letter-spacing:1px}
.news{left:666px;top:2390px;color:#fff;font-family:"Roboto Condensed",sans-serif}
.news h3{font-weight:400;font-size:24px;text-transform:uppercase}
.news .field{margin-top:12px;width:435px;height:42px;background:#fff;display:flex;align-items:center;justify-content:space-between;padding:0 8px 0 16px;font-family:"Open Sans",sans-serif;font-size:13px;color:#777}
.news .field span{background:#222;color:#fff;padding:6px 14px;font-weight:700;font-size:13px;text-transform:uppercase}

/* footer */
.footer{left:0;top:2536px;width:1200px;height:298px;background:#1e1e1e}
.foot-brand{left:97px;top:2580px;width:230px;text-align:center;color:#fff}
.foot-brand .mark{width:70px;height:70px;border-radius:50%;background:#fff;margin:0 auto}
.foot-brand .name{margin-top:8px;font-weight:700;font-size:33px;line-height:1}
.foot-about{left:97px;top:2704px;width:290px;font-size:11.5px;line-height:21px;color:#ccc}
.foot-col{top:2612px;color:#ccc;font-size:11.5px}
.foot-col h4{font-family:"Roboto Condensed",sans-serif;font-weight:400;font-size:19px;color:#fff;text-transform:uppercase;margin-bottom:20px}
.foot-col li{list-style:none;line-height:25px}
.contact li{display:flex;gap:12px;margin-bottom:12px;line-height:18px}
.subfoot{left:0;top:2834px;width:1200px;height:88px;background:#141414}
.social{left:97px;top:2865px;display:flex;gap:6px}
.social span{width:22px;height:22px;border:1px solid #aaa;border-radius:50%}
.copyright{left:0;top:2870px;width:1200px;text-align:center;font-size:11.5px;color:#ccc}
.cards{right:97px;top:2862px;display:flex;gap:6px}
.cards span{width:40px;height:26px;border-radius:3px;background:#fff}
</style>
</head>
<body>

<header>
  <div class="abs brand">
    <div class="brand-mark"></div>
    <div class="brand-name">Gizminibox</div>
  </div>
  <nav class="abs toplinks">
    <a href="#"><svg width="14" height="14" viewBox="0 0 14 14"><path d="M2 11l1-3 6-6 2 2-6 6z" fill="none" stroke="#ddd" stroke-width="1.4"/></svg>Register</a>
    <a href="#"><svg width="14" height="14" viewBox="0 0 14 14"><path d="M6 2h6v10H6M1 7h7M5 4l3 3-3 3" fill="none" stroke="#ddd" stroke-width="1.4"/></svg>Login</a>
    <a href="#"><svg width="14" height="14" viewBox="0 0 14 14"><circle cx="7" cy="4" r="3" fill="#ddd"/><path d="M1 14c0-4 3-6 6-6s6 2 6 6z" fill="#ddd"/></svg>My Account</a>
    <a href="#"><svg width="16" height="14" viewBox="0 0 16 14"><path d="M1 1h3l2 8h8l1-6H5" fill="none" stroke="#ddd" stroke-width="1.4"/><circle cx="7" cy="12" r="1.3" fill="#ddd"/><circle cx="13" cy="12" r="1.3" fill="#ddd"/></svg>My Cart</a>
    <span class="phone"><svg width="12" height="18" viewBox="0 0 12 18"><rect x="1" y="1" width="10" height="16" rx="2" fill="none" stroke="#fff" stroke-width="1.6"/></svg>0800 41 52 63</span>
  </nav>
  <nav class="abs mainnav">
    <a href="#">Home</a><a href="#">Reward Points</a><a href="#">Next Day Dispatch</a><a href="#">Coupon Codes</a><a href="#">Contact Us</a>
  </nav>
</header>

<div class="abs toolbar"></div>
<div class="abs cat-head">
  <div class="burger"><svg width="18" height="14" viewBox="0 0 18 14"><path d="M0 1h18M0 7h18M0 13h18" stroke="#fff" stroke-width="2.4"/></svg></div>
  Categories
</div>
<div class="abs search">
  <div class="q">Search Here</div>
  <div class="cats">All Categories &#8964;</div>
  <div class="go"><svg width="12" height="12" viewBox="0 0 12 12"><circle cx="5" cy="5" r="3.6" fill="none" stroke="#d33" stroke-width="1.6"/><path d="M8 8l3 3" stroke="#d33" stroke-width="1.8"/></svg></div>
</div>
<div class="abs cart">
  <div class="icon"><svg width="22" height="20" viewBox="0 0 16 14"><path d="M1 1h3l2 8h8l1-6H5" fill="none" stroke="#fff" stroke-width="1.4"/><circle cx="7" cy="12" r="1.3" fill="#fff"/><circle cx="13" cy="12" r="1.3" fill="#fff"/></svg><span class="count">0</span></div>
  0 ITEM(S) - $0.00
</div>

<ul class="abs sidebar">
  <li>New Arrival</li><li>Clearance</li><li>Barebone System</li><li>Build Your Own</li><li>Cables/ Adaptors</li><li>CD/ DVD Drives</li><li>Computer Case/ PSU</li><li>Computer System</li><li>Consumable/ FDD</li><li>Cooling/ PC Mod</li><li>CPU/ Processor</li><li>Digital Photo Frame</li><li>Digital/ Web Camera</li><li>Dot Matrix Printer</li><li>Electrical</li><li>Firewire/ SCSI/ USB</li><li>Flash Memory</li><li>Hard Disk/ Storage</li><li>HDD Enclosure</li><li>Ink/ Toner</li><li>Inkjet Printer</li><li>Keyboard/ Mouse</li><li>KVM Switches</li><li>Laser Printer</li><li>Memory/ Ram</li><li>Mobile Phone</li><li>Modem/ ADSL/ VOIP</li><li>TV Tuner/ Capture</li>
</ul>

<section class="abs slider" role="img" aria-label="Glowing circuit board city at night">
  <h2>ENTHUSIAST PC</h2>
  <p>Sed ut perspiciatis unde omnis iste natus error sit voluptatem</p>
  <span class="arrow" style="left:24px"><svg width="8" height="10" viewBox="0 0 8 10"><path d="M6 1L2 5l4 4" fill="none" stroke="#fff" stroke-width="1.6"/></svg></span>
  <span class="arrow" style="right:24px"><svg width="8" height="10" viewBox="0 0 8 10"><path d="M2 1l4 4-4 4" fill="none" stroke="#fff" stroke-width="1.6"/></svg></span>
</section>

<a class="abs promo" style="left:343px;width:370px">
  <div class="copy"><small>Shop for</small><strong>Cables/ Adaptors</strong><span class="btn">View All</span></div>
  <div class="photo" role="img" aria-label="Blue network cables plugged into a switch" style="background:linear-gradient(135deg,#3c5a78,#a9c4dc 60%,#2b3e55)"></div>
</a>
<a class="abs promo" style="left:729px;width:372px">
  <div class="copy"><small>Shop for</small><strong>Computer System</strong><span class="btn">View All</span></div>
  <div class="photo" role="img" aria-label="Close-up of a computer motherboard" style="background:linear-gradient(135deg,#4d5d6a,#9eaab5 55%,#2d3a44)"></div>
</a>

<div class="abs sec-head" style="left:343px;top:918px;width:758px">
  <span class="badge"><svg width="22" height="22" viewBox="0 0 22 22"><circle cx="11" cy="11" r="9" fill="none" stroke="#fff" stroke-width="1.6"/></svg></span>Weekly Specials
  <span class="pager"><span>&#8249;</span><span>&#8250;</span></span>
</div>
<div class="abs weekly">
  <div class="product">
    <div class="img" role="img" aria-label="Green circuit board" style="width:216px;height:178px;background:linear-gradient(135deg,#e8ece8,#5f9a6b 50%,#e8ece8)"></div>
    <p class="name">Sed ut perspiciatis unde omnis iste natus error sit</p>
    <p class="price"><b>$50.99</b> - <s>$100.99</s></p><span class="add">Add to Cart</span>
  </div>
  <div class="product">
    <div class="img" role="img" aria-label="Desktop computer set with accessories" style="width:216px;height:178px;background:linear-gradient(135deg,#f2f2f2,#3c4452 55%,#f2f2f2)"></div>
    <p class="name">Sed ut perspiciatis unde omnis iste natus error sit</p>
    <p class="price"><b>$50.99</b> - <s>$100.99</s></p><span class="add">Add to Cart</span>
  </div>
  <div class="product">
    <div class="img" role="img" aria-label="Assorted PC components" style="width:216px;height:178px;background:linear-gradient(135deg,#f2f2f2,#5a6a8a 55%,#f2f2f2)"></div>
    <p class="name">Sed ut perspiciatis unde omnis iste natus error sit</p>
    <p class="price"><b>$50.99</b> - <s>$100.99</s></p><span class="add">Add to Cart</span>
  </div>
</div>

<section class="abs panel" style="top:1375px;height:408px">
  <div class="sec-head">
    <span class="badge"><svg width="22" height="22" viewBox="0 0 22 22"><circle cx="11" cy="11" r="9" fill="none" stroke="#fff" stroke-width="1.6"/></svg></span>Best Dressed
    <span class="pager"><span>&#8249;</span><span>&#8250;</span></span>
  </div>
  <div class="grid">
    <div class="product"><div class="img" role="img" aria-label="Black motherboard" style="width:150px;height:130px;background:linear-gradient(135deg,#fff,#2b2b2b 55%,#fff)"></div><p class="stars">★★★<i>★★</i></p><p class="name">Sed ut perspiciatis unde omnis iste natus error sit</p><p class="price"><b>$50.99</b> - <s>$100.99</s></p><span class="add">Add to Cart</span></div>
    <div class="product"><span class="ribbon">Sale</span><div class="img" role="img" aria-label="Processor chip" style="width:150px;height:130px;background:linear-gradient(135deg,#fff,#8a9094 55%,#fff)"></div><p class="stars">★★★<i>★★</i></p><p class="name">Sed ut perspiciatis unde omnis iste natus error sit</p><p class="price"><b>$50.99</b> - <s>$100.99</s></p><span class="add">Add to Cart</span></div>
    <div class="product"><div class="img" role="img" aria-label="Motherboard with red slots" style="width:150px;height:130px;background:linear-gradient(135deg,#fff,#6b2a2a 55%,#fff)"></div><p class="stars">★★★<i>★★</i></p><p class="name">Sed ut perspiciatis unde omnis iste natus error sit</p><p class="price"><b>$50.99</b> - <s>$100.99</s></p><span class="add">Add to Cart</span></div>
    <div class="product"><span class="ribbon">Sale</span><div class="img" role="img" aria-label="Laptop computer" style="width:150px;height:130px;background:linear-gradient(135deg,#fff,#333 55%,#fff)"></div><p class="stars">★★★<i>★★</i></p><p class="name">Sed ut perspiciatis unde omnis iste natus error sit</p><p class="price"><b>$50.99</b> - <s>$100.99</s></p><span class="add">Add to Cart</span></div>
  </div>
</section>

<section class="abs panel" style="top:1847px;height:407px">
  <div class="sec-head">
    <span class="badge"><svg width="22" height="22" viewBox="0 0 22 22"><circle cx="11" cy="11" r="9" fill="none" stroke="#fff" stroke-width="1.6"/></svg></span>Daily Specials
    <span class="pager"><span>&#8249;</span><span>&#8250;</span></span>
  </div>
  <div class="grid">
    <div class="product"><div class="img" role="img" aria-label="Compact motherboard" style="width:150px;height:130px;background:linear-gradient(135deg,#fff,#3a3a3a 55%,#fff)"></div><p class="stars">★★★<i>★★</i></p><p class="name">Sed ut perspiciatis unde omnis iste natus error sit</p><p class="price"><b>$50.99</b> - <s>$100.99</s></p><span class="add">Add to Cart</span></div>
    <div class="product"><span class="ribbon">20% Save</span><div class="img" role="img" aria-label="Green circuit board with components" style="width:150px;height:130px;background:linear-gradient(135deg,#fff,#5f8f5a 55%,#fff)"></div><p class="stars">★★★<i>★★</i></p><p class="name">Sed ut perspiciatis unde omnis iste natus error sit</p><p class="price"><b>$50.99</b> - <s>$100.99</s></p><span class="add">Add to Cart</span></div>
    <div class="product"><div class="img" role="img" aria-label="Hard drive with ribbon cable" style="width:150px;height:130px;background:linear-gradient(135deg,#fff,#8a7a6a 55%,#fff)"></div><p class="stars">★★★<i>★★</i></p><p class="name">Sed ut perspiciatis unde omnis iste natus error sit</p><p class="price"><b>$50.99</b> - <s>$100.99</s></p><span class="add">Add to Cart</span></div>
    <div class="product"><span class="ribbon">20% Save</span><div class="img" role="img" aria-label="LCD display module on a board" style="width:150px;height:130px;background:linear-gradient(135deg,#fff,#2f4f8a 55%,#fff)"></div><p class="stars">★★★<i>★★</i></p><p class="name">Sed ut perspiciatis unde omnis iste natus error sit</p><p class="price"><b>$50.99</b> - <s>$100.99</s></p><span class="add">Add to Cart</span></div>
  </div>
</section>

<section class="abs band"><div class="free"></div></section>
<div class="abs free-txt"><b>FREE<br>SHIPPING</b><span>WE ALWAYS GUARANTEE</span></div>
<svg class="abs" style="left:395px;top:2395px" width="140" height="90" viewBox="0 0 140 90" aria-hidden="true">
  <path d="M0 18h22M6 34h16M0 50h22" stroke="#fff" stroke-width="5"/>
  <rect x="30" y="8" width="62" height="52" rx="3" fill="#fff"/>
  <path d="M96 24h22l16 20v16H96z" fill="#fff"/>
  <circle cx="50" cy="68" r="10" fill="#fff" stroke="#33b8a4" stroke-width="4"/>
  <circle cx="114" cy="68" r="10" fill="#fff" stroke="#33b8a4" stroke-width="4"/>
</svg>
<div class="abs news">
  <h3>Newsletter Sign Up</h3>
  <div class="field">Enter Email Address <span>Sign Up</span></div>
</div>

<footer>
  <div class="abs footer"></div>
  <div class="abs foot-brand"><div class="mark"></div><div class="name">Gizminibox</div></div>
  <p class="abs foot-about">Sed ut perspiciatis unde omnis iste natus error sit voluptatem accusantium doloremque laudantium, totam rem aperiam, eaque ipsa quae ab</p>
  <div class="abs foot-col contact" style="left:449px;width:260px">
    <h4>Contact Us</h4>
    <ul>
      <li><svg width="12" height="16" viewBox="0 0 12 16"><path d="M6 15S1 9 1 6a5 5 0 0110 0c0 3-5 9-5 9z" fill="#ccc"/><circle cx="6" cy="6" r="2" fill="#1e1e1e"/></svg><span>Gizminibox<br>Lindenweg Str. 27 50321 Rheinfeld<br>Germany</span></li>
      <li><svg width="12" height="14" viewBox="0 0 12 14"><path d="M2 1l3 1 1 3-2 1c1 2 2 3 4 4l1-2 3 1 0 3c-6 1-11-4-10-11z" fill="#ccc"/></svg><span>Phone: +49-300-47-21-096</span></li>
      <li><svg width="14" height="12" viewBox="0 0 14 12"><rect x="1" y="2" width="12" height="9" fill="#ccc"/><path d="M1 2l6 5 6-5" fill="none" stroke="#1e1e1e" stroke-width="1.2"/></svg><span>Email: mail@Gizminibox.com.au</span></li>
    </ul>
  </div>
  <div class="abs foot-col" style="left:758px">
    <h4>Customer Service</h4>
    <ul><li>About Us</li><li>Term &amp; Condition of Use</li><li>Term &amp; Condition of Sale</li><li>Privacy Statement</li><li>Affiliates</li></ul>
  </div>
  <div class="abs foot-col" style="left:994px">
    <h4>Quick Links</h4>
    <ul><li>My Account</li><li>Order History</li><li>Wishlist</li><li>Returns</li><li>Freight Policy</li></ul>
  </div>
  <div class="abs subfoot"></div>
  <div class="abs social"><span></span><span></span><span></span><span></span></div>
  <p class="abs copyright">©2017 Gizminibox. All Rights Reserved.</p>
  <div class="abs cards"><span></span><span></span><span></span><span></span></div>
</footer>

</body>
</html>
```